Bold Cover needed for a book on Workplace Bullying

I need a book cover design for a book titled, “Iron Silence?” The book recounts my story of bullying in the workplace. It also includes chapters on how readers can minimize/stop workplace bullying, write an effective complaint, and ensure their own mental wellbeing.
I am looking for a bold design using red and black, and possibly distressed lettering. The covers of other books dealing with this subject do not reflect my vision. They are often too childish or look too academic. This book needs to stress the serious nature of a toxic workplace, while appealing to readers experiencing a similar situation. I’d like the cover to reflect the mental anguish associated with workplace bullying (hence the distressed lettering).
I have included a cover that appeals to me (although the coloring is wrong). That said, I am also very happy (and excited) to see your creative input!
On the cover, it should have the following:
Title: Iron Silence?
Subtitle: How the Harbour Works Department Condones Bullying & Ruins Lives
Author: Owen Frick
Other relevant details:
Book size: 5.5” x 8.5”
Back cover will have a blurb, author picture/short bio, and barcode
The blurb on the back cover reads:
Undermining, intimidation and threats
Despite the Department of Harbour Works allegedly holding a zero tolerance for bullying, these behaviours were an everyday occurrence in at least one workplace. Even after a decade of complaints, numerous witnesses and physical proof, the department failed to act. Instead, they looked the other way, allowing one powerful and well-connected individual to end careers and ruin lives.
After being targeted, one teacher resolved to put an end to the abuse experienced by more than fifty employees. His startling story reveals the relentless bullying, mental health ramifications, and insidious tactics used to cover up the corrosive behaviour.
Those who have experienced a toxic workplace will also find much needed support and guidance, intended to minimise suffering and detail a clear way forward. Chapters include dealing with bullying in the workplace, how to lodge a successful complaint, and how to stay sane during any potential legal action.

```html
<!DOCTYPE html>
<html lang="en">
<head>
<meta charset="utf-8">
<title>Iron Silence? — Book Cover</title>
<link rel="stylesheet" href="https://fonts.googleapis.com/css2?family=Open+Sans:wght@400;600;800&family=Josefin+Sans:wght@300&family=Playfair+Display:wght@400&family=Allura&display=swap">
<style>
  :root {
    --stage: #262626;
    --black: #0b0b0b;
    --ink: #1a1a1a;
    --red: #f01a1a;
    --red-bright: #ff2a2a;
    --red-deep: #b80f0f;
  }
  * { box-sizing: border-box; margin: 0; padding: 0; }
  html, body {
    width: 1200px; height: 960px; overflow: hidden;
    background: var(--stage);
  }
  .spread {
    position: absolute; left: 52px; top: 80px;
    width: 1096px; height: 800px;
    display: flex;
  }
  /* Back cover */
  .back-cover {
    width: 518px; height: 800px;
    background: var(--black);
    color: var(--red);
    text-align: center;
    padding: 40px 52px 0;
  }
  .back-cover .tag {
    font-family: "Allura", cursive;
    font-size: 78px; line-height: 1;
    margin-bottom: 44px;
  }
  .back-cover .blurb {
    font-family: "Playfair Display", serif;
    font-size: 14.5px; line-height: 1.22;
    margin-bottom: 40px;
  }
  /* Spine */
  .spine {
    width: 60px; height: 800px;
    background: var(--black);
    display: flex; align-items: center; justify-content: center;
  }
  .spine .spine-author {
    writing-mode: vertical-rl; transform: rotate(180deg);
    font-family: "Playfair Display", serif;
    color: var(--red); font-size: 24px; letter-spacing: 2px;
    white-space: nowrap;
  }
  /* Front cover */
  .front-cover {
    position: relative;
    width: 518px; height: 800px;
    background: linear-gradient(160deg, var(--red-bright), var(--red) 60%, var(--red-deep));
    overflow: hidden;
  }
  .cover-artwork {
    position: absolute; inset: 0;
    background: linear-gradient(180deg, rgba(11,11,11,0.15) 0%, rgba(11,11,11,0.75) 50%, var(--black) 72%);
    clip-path: polygon(80% 2%, 100% 2%, 100% 82%, 0 88%, 0 68%, 58% 64%, 72% 46%, 82% 24%);
  }
  .title {
    position: absolute; left: 18px; top: 92px;
    font-family: "Open Sans", sans-serif; font-weight: 800;
    color: var(--ink); line-height: 0.85;
  }
  .title .title-main { display: block; font-size: 148px; letter-spacing: -7px; }
  .title .title-sub { display: block; font-size: 52px; letter-spacing: -2px; margin-top: 8px; }
  .subtitle {
    position: absolute; left: 24px; top: 370px; width: 300px;
    font-family: "Open Sans", sans-serif; color: var(--ink);
    line-height: 1.1;
  }
  .subtitle .line { display: block; }
  .subtitle .strong { font-weight: 800; font-size: 32px; }
  .subtitle .light { font-weight: 400; font-size: 19px; }
  .author {
    position: absolute; left: 0; right: 0; bottom: 34px;
    text-align: center;
    font-family: "Josefin Sans", sans-serif; font-weight: 300;
    font-size: 52px; letter-spacing: 2px; color: var(--ink);
  }
</style>
</head>
<body>
  <main class="spread">
    <section class="back-cover">
      <p class="tag">Free</p>
      <p class="blurb">Lorem ipsum dolor sit amet, consectetur adipiscing elit, sed do eiusmod tempor incididunt ut labore et dolore magna aliqua. Quis ipsum suspendisse ultrices gravida. Risus commodo viverra maecenas accumsan lacus vel facilisis. Lore incididunt ut labore et dolore magna aliqua. Quis ipsum suspendisse ultrices gravida. Risus commodo viverra maecenas accumsan lacus vel facilisis.</p>
      <p class="blurb">Lorem ipsum dolor sit amet, consectetur adipiscing elit, sed do eiusmod tempor incididunt ut labore et dolore magna aliqua. Quis ipsum suspendisse ultrices gravida. Risus commodo viverra maecenas accumsan lacus vel facilisis.</p>
      <p class="blurb">Lorem ipsum dolor sit amet, consectetur adipiscing elit, sed do eiusmod tempor incididunt ut labore et dolore magna aliqua. Quis ipsum suspendisse ultrices gravida. Risus commodo viverra maecenas accumsan lacus vel facilisis. Lorem ipsum dolor sit amet, consectetur adipiscing elit, sed do eiusmod tempor incididunt ut labore et dolore magna aliqua. Quis ipsum suspendisse ultrices gravida. Risus commodo viverra maecenas accumsan lacus vel facilisis.</p>
      <p class="blurb">Lorem ipsum dolor sit ae ultrices gravida. Risus commodo viverra maecenas accumsan lacus vel facilisis.</p>
    </section>
    <section class="spine">
      <span class="spine-author">OWEN FRICK</span>
    </section>
    <section class="front-cover">
      <div class="cover-artwork" role="img" aria-label="Cover artwork area: dark silhouette artwork rising from the lower edge up the right side of the red field"></div>
      <h1 class="title">
        <span class="title-main">IRON</span>
        <span class="title-sub">SILENCE?</span>
      </h1>
      <p class="subtitle">
        <span class="line"><span class="strong">HOW</span> <span class="light">THE HARBOUR WORKS</span></span>
        <span class="line light">DEPARTMENT</span>
        <span class="line strong">CONDONES</span>
        <span class="line"><span class="light">BULLYING &amp;</span> <span class="strong">RUINS</span></span>
        <span class="line strong">LIVES</span>
      </p>
      <p class="author">OWEN FRICK</p>
    </section>
  </main>
</body>
</html>
```